Best in class cloud software provider for retailers needs a new business card design to reflect prod

We are a software company based out of Chicago selling into retailers. We have a new website and marketing collateral that support our new product designs. We are obsessed with simplicity, ease of use, and having a really powerful product set. We have two products as noted on our website - www.brolvane.com - one is a retail task management product and the other is a Help Ticketing product.

At Brolvane we are passionate about creating the best Retail Task Management system in the industry. We bring more than 20 years of retail operations, Workforce Management and Retail Task experience and have a set of web and mobile software features that no one else has. Brolvane enables you to plan and distribute work throughout your organization and ensure it gets done.

We need a new business card design that reflects our new branding, message and approach.

I've attached a few documents that help support what we are building and how our colors look.

There may be additional future work if this goes well.

Thanks,
Mark

President

Target Market(s)

We sell into retailers and are a software company

Industry/Entity Type

Software

Contact Information for Business Card

The card must have

Name
title
address
tele
email
Brolvane logo (someplace)

So for example

It would have for me

Mark Dorsett
President
48 West Harlow Ave. Suite 310
Chicago, IL 60687
3125550187
mdorsett@brolvane.com

Requirements
Must have
• We need to cards for 5 different people - same design different names etc
Nice to have
• should reflect our colors and product and website - be creative - ease of use, simplicity, and power is what the product is about - but we are very forward Brolvane and hear all the time that our product is gorgeous. The font should be consistent with our website, and marketing one pager included
Should not have
• Strange or unfamiliar colors or fonts...

```html
<!DOCTYPE html>
<html lang="en">
<head>
<meta charset="utf-8">
<title>Brolvane Business Card</title>
<link href="https://fonts.googleapis.com/css2?family=Open+Sans:wght@400;600;700&display=swap" rel="stylesheet">
<style>
  :root {
    --page-bg: #e9ebed;
    --brand-blue: #1d78a6;
    --brand-blue-deep: #14587f;
    --brand-blue-light: #3d93bf;
    --card-white: #ffffff;
    --fold-grey: #e6e8ea;
    --ink-light: #f2f8fb;
  }
  * { margin: 0; padding: 0; box-sizing: border-box; }
  html, body { width: 1200px; height: 950px; overflow: hidden; }
  body {
    background: var(--page-bg);
    font-family: "Open Sans", Arial, sans-serif;
    position: relative;
  }
  .card {
    position: absolute;
    left: 250px;
    width: 700px;
    height: 400px;
    overflow: hidden;
    box-shadow: 0 8px 24px rgba(0,0,0,0.18);
  }
  .card-front { top: 40px; background: var(--card-white); }
  .card-back {
    top: 500px;
    background: linear-gradient(100deg, var(--brand-blue) 0%, var(--brand-blue) 55%, var(--brand-blue-deep) 100%);
  }
  .front-shapes { position: absolute; inset: 0; }
  .brand-name {
    position: absolute;
    left: 70px;
    top: 160px;
    font-size: 56px;
    font-weight: 700;
    color: var(--brand-blue);
    letter-spacing: -1px;
  }
  .contact {
    position: absolute;
    left: 430px;
    top: 62px;
    color: var(--ink-light);
    font-size: 17px;
    line-height: 1.35;
  }
  .contact-name { font-size: 23px; font-weight: 700; letter-spacing: 0.3px; }
  .contact-title { font-size: 17px; margin-bottom: 26px; }
  .contact-line { display: flex; align-items: center; gap: 8px; }
  .contact-line svg { width: 16px; height: 16px; flex: none; }
  .back-brand {
    position: absolute;
    left: 0; right: 0;
    top: 130px;
    text-align: center;
    color: var(--card-white);
    font-size: 52px;
    font-weight: 700;
    letter-spacing: -1px;
  }
  .back-web {
    position: absolute;
    left: 0; right: 0;
    top: 245px;
    text-align: center;
    color: var(--ink-light);
    font-size: 20px;
    letter-spacing: 3px;
  }
</style>
</head>
<body>

  <section class="card card-front" aria-label="Business card front">
    <svg class="front-shapes" viewBox="0 0 700 400" width="700" height="400" aria-hidden="true">
      <defs>
        <linearGradient id="panelBlue" x1="0" y1="0" x2="1" y2="1">
          <stop offset="0" stop-color="#3d93bf"/>
          <stop offset="0.45" stop-color="#1d78a6"/>
          <stop offset="1" stop-color="#14587f"/>
        </linearGradient>
      </defs>
      <polygon points="380,400 700,400 700,330" fill="#e6e8ea"/>
      <polygon points="395,0 700,0 700,400 455,400 395,290" fill="url(#panelBlue)"/>
    </svg>

    <div class="brand-name">Brolvane</div>

    <div class="contact">
      <div class="contact-name">Mark Dorsett</div>
      <div class="contact-title">President</div>
      <div>48 West Harlow Ave.</div>
      <div>Suite 310</div>
      <div>Chicago, IL 60687</div>
      <div class="contact-line">
        <svg viewBox="0 0 16 16" aria-hidden="true"><path d="M4 1.5l2.2 3-1.3 1.5c.8 1.8 2.3 3.3 4.1 4.1l1.5-1.3 3 2.2-1.2 2.5C7.5 13.5 2.5 8.5 1.5 2.7z" fill="#f2f8fb"/></svg>
        <span>3125550187</span>
      </div>
      <div class="contact-line">
        <svg viewBox="0 0 16 16" aria-hidden="true"><rect x="1" y="3.5" width="14" height="9" fill="#f2f8fb"/><path d="M1 3.5l7 5 7-5" fill="none" stroke="#1d78a6" stroke-width="1.3"/></svg>
        <span>mdorsett@brolvane.com</span>
      </div>
      <div class="contact-line">
        <svg viewBox="0 0 16 16" aria-hidden="true"><circle cx="8" cy="8" r="6.5" fill="#f2f8fb"/><path d="M1.5 8h13M8 1.5c-2.5 3-2.5 10 0 13M8 1.5c2.5 3 2.5 10 0 13" fill="none" stroke="#1d78a6" stroke-width="1"/></svg>
        <span>www.brolvane.com</span>
      </div>
    </div>
  </section>

  <section class="card card-back" aria-label="Business card back">
    <div class="back-brand">Brolvane</div>
    <div class="back-web">www.brolvane.com</div>
  </section>

</body>
</html>
```